High end boutique food product label

We are looking for a label design to be used on our range of high end food products. We don't have a design or colour scheme in mind and are interested to see what ideas are submitted.
We would like it to feel sophisticated, chic, and eye-catching.
All of our products are handmade in Australia using Australian ingredients.
The graphics for the label will need to be scaleable to be fit a variety of labels from small squat jars with labels sized 3.5cm high and 7cm wide, to tall thin bottles with labels that are 14cm high and 4.5cm wide.
We would be interested in working with the winning designer to create these different sized labels.
The label submitted for this project should be 14cm high and 4.5cm wide, it should include our logo (file supplied in .jpeg and .ai), the product name 'Extra Virgin Olive Oil' and the size '250ml'.
This is just the front label on a bottle, we are not expecting a rear label to be created currently.
You are welcome to use any fonts you think will look good but the fonts used in our logo are Allaina Medium and Bebas Kai Regular.

```html
<!DOCTYPE html>
<html lang="en">
<head>
<meta charset="utf-8">
<title>Larkfield Pantry – Extra Virgin Olive Oil Label</title>
<link href="https://fonts.googleapis.com/css2?family=Lora:wght@500&family=Pinyon+Script&display=swap" rel="stylesheet">
<style>
  :root {
    --backdrop: #f4f4f2;
    --label-black: #050505;
    --gold: #b8975a;
    --gold-soft: rgba(184, 151, 90, 0.55);
    --gold-faint: rgba(138, 109, 59, 0.22);
  }
  * { box-sizing: border-box; margin: 0; padding: 0; }
  html, body {
    width: 1070px;
    height: 1200px;
    overflow: hidden;
    background: var(--backdrop);
  }
  .canvas {
    position: relative;
    width: 1070px;
    height: 1200px;
  }
  .label {
    position: absolute;
    left: 355px;
    top: 55px;
    width: 360px;
    height: 1090px;
    background: var(--label-black);
    border-radius: 180px 180px 0 0 / 170px 170px 0 0;
    overflow: hidden;
    color: var(--gold);
    font-family: "Lora", Georgia, serif;
    font-weight: 500;
  }
  .brand-name {
    position: absolute;
    top: 180px;
    left: 0;
    width: 100%;
    text-align: center;
    line-height: 1;
  }
  .brand-line-main { display: block; font-size: 58px; }
  .brand-line-sub { display: block; font-size: 34px; margin-top: 4px; }
  .rule {
    position: absolute;
    left: 0;
    width: 100%;
    height: 7px;
    background: var(--gold);
  }
  .rule-top { top: 412px; }
  .rule-bottom { top: 553px; }
  .product-name {
    position: absolute;
    top: 434px;
    left: 0;
    width: 100%;
    text-align: center;
    font-weight: 500;
  }
  .product-variety {
    display: block;
    font-family: "Pinyon Script", cursive;
    font-size: 54px;
    line-height: 1.05;
  }
  .product-type {
    display: block;
    font-family: "Lora", Georgia, serif;
    font-weight: 500;
    font-size: 34px;
    line-height: 1.2;
    margin-top: 2px;
  }
  .origin-badge {
    position: absolute;
    top: 582px;
    left: 126px;
    width: 100px;
    height: 100px;
  }
  .olive-branch {
    position: absolute;
    left: 0;
    top: 700px;
    width: 100%;
    height: 390px;
    background:
      radial-gradient(ellipse 60% 55% at 35% 75%, var(--gold-soft), transparent 75%),
      radial-gradient(ellipse 45% 60% at 75% 40%, var(--gold-faint), transparent 80%),
      linear-gradient(200deg, transparent 10%, var(--gold-faint) 60%, rgba(184,151,90,0.35) 100%);
  }
  .net-volume {
    position: absolute;
    right: 10px;
    bottom: 8px;
    font-size: 18px;
    color: var(--gold);
  }
</style>
</head>
<body>
<main class="canvas">
  <section class="label">
    <div class="brand-name">
      <span class="brand-line-main">Larkfield</span>
      <span class="brand-line-sub">Pantry</span>
    </div>

    <div class="rule rule-top"></div>
    <h1 class="product-name">
      <span class="product-variety">Extra Virgin</span>
      <span class="product-type">Olive Oil</span>
    </h1>
    <div class="rule rule-bottom"></div>

    <svg class="origin-badge" viewBox="0 0 100 100" aria-hidden="true">
      <circle cx="50" cy="50" r="46" fill="none" stroke="var(--gold)" stroke-width="2"/>
      <circle cx="50" cy="50" r="36" fill="var(--gold)" fill-opacity="0.25"/>
    </svg>

    <div class="olive-branch" role="img" aria-label="Gold line drawing of an olive branch with leaves and olives rising from the lower left"></div>

    <span class="net-volume">250ml</span>
  </section>
</main>
</body>
</html>
```